Create a Graphic About YOURSELF and PixelHarbor

PixelHarbor would like you (designers) to create an awesome graphic to promote YOURSELF and your profile on PixelHarbor!

Your graphic should communicate your name, your services and should mention PixelHarbor.

The design should be perfect for sharing on Chatterly. Here's an example of what we'd like http://blog.pixelharbor-example.ca/article/333/pixelharbor-launches-3000-hire-me-social-design-contest

Once you submitted your design, we'd love you to share the design ('advertisement') and promote yourself and PixelHarbor to your friends and potential customers. So make your submissions great and get your friends to vote for your design by 'Liking' it on Chatterly!

Prizes:
$1500 - "PixelHarbor Community" prize awarded to the designer with the most Chatterly 'Likes'
5 x $50 for the next 5 'most liked' designs on Chatterly

$1000 - "Hire Me" prize awarded to the designer who receives the most client invites
5 x $50 for the next 5 'most invited' designers

In summary, this is a great opportunity for you to increase your exposure to PixelHarbor customers and win cash prizes. Show off your design skills and get hired by PixelHarbor customers from around the world!

Target Market(s)

Fans, friends and customers of YOU

Industry/Entity Type

Cash

Requirements
Must have
• 1) Include your PixelHarbor user name on the graphic so customers can find you in the PixelHarbor Designer Directory
2) Include the tagline "Hire Me on PixelHarbor.com!" in your graphic design.
3) Share your design's URL on our Chatterly wall at http://chatterly-example.com/pixelharbor and get your friends to 'like' your design.
Nice to have
• 1) Include a tagline that expresses your design approach/philosophy
2) Artwork dimensions: 403 x 403 px
3) You can submit more than 1 design!
Should not have
• You must own the copyright of any images you use including stock imagery.

```html
<!DOCTYPE html>
<html lang="en">
<head>
<meta charset="utf-8">
<title>Hire Me on PixelHarbor.com – Tavo</title>
<link rel="stylesheet" href="https://fonts.googleapis.com/css2?family=Bebas+Neue&family=Raleway:wght@200&family=Montserrat:wght@900&family=Josefin+Sans:wght@600&family=Oswald:wght@400&display=swap">
<style>
  :root {
    --cardboard: #a97b4c;
    --cardboard-light: #b48755;
    --ink-brown: #2b1a0d;
    --paper-white: #ffffff;
    --sun-yellow: #fbc40d;
    --mint-green: #63b07f;
    --bubble-black: #111111;
    --sketch-dark: #3a2614;
  }
  html, body {
    margin: 0;
    padding: 0;
    overflow: hidden;
  }
  .poster {
    position: relative;
    width: 998px;
    height: 1200px;
    overflow: hidden;
    background: radial-gradient(ellipse at 50% 40%, var(--cardboard-light), var(--cardboard) 75%);
  }
  .headline {
    position: absolute;
    margin: 0;
    white-space: nowrap;
    line-height: 1;
  }
  .headline--still {
    left: 75px;
    top: 42px;
    font-family: "Bebas Neue", sans-serif;
    font-size: 132px;
    letter-spacing: 20px;
    color: var(--ink-brown);
  }
  .headline--for {
    left: 93px;
    top: 190px;
    font-family: "Bebas Neue", sans-serif;
    font-size: 117px;
    letter-spacing: 9px;
    color: var(--ink-brown);
  }
  .headline--perfect {
    left: 477px;
    top: 181px;
    font-family: "Raleway", sans-serif;
    font-weight: 200;
    font-size: 135px;
    color: var(--paper-white);
    transform: scaleX(0.76);
    transform-origin: left top;
  }
  .headline--role {
    left: 112px;
    top: 328px;
    font-family: "Montserrat", sans-serif;
    font-weight: 900;
    font-size: 136px;
    line-height: 120px;
    letter-spacing: -2px;
    color: var(--sun-yellow);
    transform: scaleX(0.87);
    transform-origin: left top;
  }
  .question-art {
    position: absolute;
    left: 750px;
    top: 352px;
    width: 150px;
    height: 233px;
  }
  .intro {
    position: absolute;
    left: 125px;
    top: 626px;
    margin: 0;
    font-family: "Josefin Sans", sans-serif;
    font-weight: 600;
    font-size: 46px;
    letter-spacing: 2.2px;
    color: var(--paper-white);
    white-space: nowrap;
  }
  .designer-name {
    position: absolute;
    left: 0;
    width: 998px;
    top: 717px;
    margin: 0;
    text-align: center;
    font-family: "Montserrat", sans-serif;
    font-weight: 900;
    font-size: 250px;
    line-height: 1;
    letter-spacing: -4px;
    color: var(--mint-green);
  }
  .hire-bubble {
    position: absolute;
    left: 0;
    top: 1010px;
    width: 480px;
    height: 190px;
  }
  .hire-bubble__text {
    position: absolute;
    left: 165px;
    top: 1030px;
    width: 300px;
    margin: 0;
    text-align: center;
    font-family: "Oswald", sans-serif;
    font-size: 40px;
    line-height: 1.2;
    color: var(--paper-white);
  }
</style>
</head>
<body>
<main class="poster">
  <h1 class="headline headline--still">Still Looking</h1>
  <p class="headline headline--for">For the</p>
  <p class="headline headline--perfect">PERFECT</p>
  <p class="headline headline--role">GRAPHIC<br>DESIGNER</p>

  <svg class="question-art" viewBox="0 0 150 233" role="img" aria-label="Hand-sketched question mark with cross-hatched shading">
    <rect x="0" y="0" width="150" height="233" rx="55" fill="var(--sketch-dark)" opacity="0.35"/>
  </svg>

  <p class="intro">You’d rather remember my name :</p>

  <p class="designer-name">Tavo</p>

  <svg class="hire-bubble" viewBox="0 0 480 190" aria-hidden="true">
    <ellipse cx="304" cy="72" rx="176" ry="58" fill="var(--bubble-black)"/>
    <path d="M190 112 C150 140 110 145 80 155 C55 163 45 180 60 177 C72 175 60 161 40 167 C20 173 10 182 0 186 L0 174 C20 166 35 156 55 151 C95 142 140 132 170 102 Z" fill="var(--bubble-black)"/>
  </svg>
  <p class="hire-bubble__text">Hire me now on<br>PixelHarbor.com !</p>
</main>
</body>
</html>
```